Harbor Fieldworks (Business Card Design)

Need business cards designed. Something modern, chic, and sleek. Mabye the back of the card should be the navy blue that is in the logo and then just the logo on the back.

Target Market(s)

Those in the hotel, office, and renovation industry

Contact Information for Business Card

1. Logo 2. Dorian Velasko 3. CEO/Founder 4. Phone: (833) HarbFld / (833) 427-2353 5. Email: dorian@theharborfieldworks.com 6. Website: www.theharborfieldworks.com

Font styles to use
Other font styles liked:
• Look at the logo font and base the font for everything else off of that.

Colors
0054AA
0677BA
7BADD7
CADEEF
E8F1F8

Requirements
Must have
• Colors that are associated in the logo
Nice to have
• Sleek modern clean and chic design.

```html
<!DOCTYPE html>
<html lang="en">
<head>
<meta charset="utf-8">
<title>Harbor Fieldworks — Business Card</title>
<link href="https://fonts.googleapis.com/css2?family=Montserrat:wght@500&family=Open+Sans:wght@400;700&display=swap" rel="stylesheet">
<style>
  :root {
    --backdrop: #e9e6e1;
    --card-navy: #121c3a;
    --card-navy-deep: #0b1330;
    --card-navy-light: #1f2d55;
    --gold: #b8832c;
    --text-light: #cfcac2;
    --brand-light: #d9d3c8;
  }
  html, body {
    margin: 0;
    padding: 0;
    width: 1200px;
    height: 1047px;
    overflow: hidden;
    background: var(--backdrop);
  }
  .card {
    position: absolute;
    left: 80px;
    top: 240px;
    width: 1040px;
    height: 567px;
    border-radius: 24px;
    background:
      radial-gradient(ellipse at 20% 70%, var(--card-navy-light) 0%, transparent 55%),
      linear-gradient(135deg, var(--card-navy) 0%, var(--card-navy-deep) 100%);
    box-shadow: 0 18px 40px rgba(0,0,0,0.18);
    font-family: "Open Sans", sans-serif;
  }
  .brand {
    position: absolute;
    left: 28px;
    top: 190px;
    width: 400px;
    text-align: center;
  }
  .brand-square {
    width: 22px;
    height: 22px;
    margin: 0 auto 22px;
    background: var(--gold);
  }
  .brand-name {
    font-family: "Montserrat", sans-serif;
    font-weight: 500;
    font-size: 36px;
    letter-spacing: 3px;
    line-height: 1.2;
    text-transform: uppercase;
    color: var(--brand-light);
  }
  .divider {
    position: absolute;
    left: 416px;
    top: 182px;
    width: 3px;
    height: 210px;
    background: var(--gold);
  }
  .details {
    position: absolute;
    left: 458px;
    top: 172px;
    color: var(--text-light);
  }
  .person-name {
    font-weight: 700;
    font-size: 38px;
    color: var(--gold);
    margin: 0;
    line-height: 1.1;
  }
  .person-title {
    font-size: 26px;
    margin: 6px 0 38px;
  }
  .contact-list {
    list-style: none;
    margin: 0;
    padding: 0;
    font-size: 26px;
    line-height: 36px;
  }
  .contact-item {
    display: flex;
    align-items: center;
    gap: 8px;
  }
  .contact-icon {
    width: 22px;
    height: 22px;
    fill: var(--gold);
    flex: none;
  }
</style>
</head>
<body>
  <section class="card">
    <div class="brand">
      <div class="brand-square"></div>
      <div class="brand-name">Harbor<br>Fieldworks</div>
    </div>
    <div class="divider"></div>
    <div class="details">
      <h1 class="person-name">Dorian Velasko</h1>
      <div class="person-title">Founder + CEO</div>
      <ul class="contact-list">
        <li class="contact-item">
          <svg class="contact-icon" viewBox="0 0 24 24"><path d="M6.6 10.8c1.4 2.8 3.8 5.1 6.6 6.6l2.2-2.2c.3-.3.7-.4 1-.2 1.1.4 2.3.6 3.6.6.6 0 1 .4 1 1V20c0 .6-.4 1-1 1C10.6 21 3 13.4 3 4c0-.6.4-1 1-1h3.5c.6 0 1 .4 1 1 0 1.3.2 2.5.6 3.6.1.3 0 .7-.2 1z"/></svg>
          <span>(833) 427-2353</span>
        </li>
        <li class="contact-item">
          <svg class="contact-icon" viewBox="0 0 24 24"><path d="M3 6h18v2l-9 5.5L3 8z"/><path d="M3 10l9 5.5 9-5.5v8H3z"/></svg>
          <span>dorian@theharborfieldworks.com</span>
        </li>
        <li class="contact-item">
          <svg class="contact-icon" viewBox="0 0 24 24"><path d="M12 2a10 10 0 1 0 0 20 10 10 0 0 0 0-20zm-1 17.9A8 8 0 0 1 4.1 11H7c0 3 1.3 6.3 4 8.9zM7 9H4.4A8 8 0 0 1 11 4.1C9 6 7.8 7.5 7 9zm6 10.9c2.7-2.6 4-5.9 4-8.9h2.9a8 8 0 0 1-6.9 8.9zM17 9c-.8-1.5-2-3-4-4.9A8 8 0 0 1 19.6 9z"/></svg>
          <span>www.theharborfieldworks.com</span>
        </li>
      </ul>
    </div>
  </section>
</body>
</html>
```